Chiropractic Business /Appointment Card Design

We are a wellness based well est. chiropractic under new ownership. I have logo with old name looking to change up with new name, maybe design. I like three people logo but I don't like colors or name layout. Looking for ideas, thinking Maroon(more red then brown) and/ or metallic Gold, silver, bronze. I would like to incorporate design and layouts on business cards for other employees, letterhead, envelopes, magnets, etc.

Target Market(s)

0-65 wellness minded

Industry/Entity Type

Business

Contact Information for Business Card

Maple Ridge Family Chiropractic
Dr. Warren Balfour
Chiropractor
214 Pellham R. Road
Alder Falls, NY 13752
607-555-0184
www.vitalspringcare.com
Office Hours:
Monday 9-12, 2:30-5
Tuesday 2:30-6
Wednesday 9-12, 2:30-5
Thursday 9-12, 2:30-6
Date Time
______ _______
______ _______
______ ______
______ ______
______ ______

Requirements
Must have
• three people (attached)

```html
<!DOCTYPE html>
<html lang="en">
<head>
<meta charset="utf-8">
<title>Maple Ridge Family Chiropractic – Business Card</title>
<link href="https://fonts.googleapis.com/css2?family=Cinzel:wght@400;700&family=Open+Sans:wght@400;600&display=swap" rel="stylesheet">
<style>
  :root {
    --board: #e1e1e1;
    --maroon: #7a2626;
    --gold: #c9a24e;
    --gold-dark: #9c7a2e;
    --gold-light: #e3c57a;
    --white: #ffffff;
    --ink-dark: #6a1f1f;
  }
  * { margin: 0; padding: 0; box-sizing: border-box; }
  html, body { width: 1200px; height: 927px; overflow: hidden; background: var(--board); }
  .board { position: relative; width: 1200px; height: 927px; }

  .card {
    position: absolute;
    width: 599px; height: 346px;
    background: var(--maroon);
    box-shadow: 0 2px 5px rgba(0,0,0,.3);
    overflow: hidden;
  }
  .card--front { left: 45px; top: 79px; }
  .card--back { left: 556px; top: 503px; }

  .brand {
    position: absolute; left: 0; width: 100%;
    text-align: center;
    font-family: "Cinzel", serif; font-weight: 400;
    color: var(--gold-light);
    line-height: 1.15;
  }
  .brand__dot {
    display: block; margin: 0 auto 12px;
    width: 60px; height: 60px; border-radius: 50%;
    background: var(--gold);
  }
  .brand__name { font-size: 22px; letter-spacing: .6px; }
  .brand__sub { font-size: 14.5px; letter-spacing: 1px; }
  .card--front .brand { top: 30px; }
  .card--back .brand { top: 60px; color: var(--gold); }
  .card--back .brand__dot { background: var(--gold-dark); }

  .gold-band {
    position: absolute; left: 0; top: 166px; width: 100%; height: 10px;
    background: linear-gradient(90deg, var(--gold-dark), var(--gold-light) 50%, var(--gold-dark));
  }

  .doctor {
    position: absolute; left: 0; top: 190px; width: 100%;
    text-align: center;
    font-family: "Cinzel", serif; font-weight: 700;
    font-size: 19.5px; color: var(--white); letter-spacing: .2px;
  }

  .contact { position: absolute; left: 200px; top: 222px; list-style: none;
    font-family: "Open Sans", sans-serif; font-size: 12.5px; color: var(--white); }
  .contact__item { position: absolute; left: 0; display: flex; align-items: flex-start; white-space: nowrap; }
  .contact__item svg { width: 23px; height: 23px; flex: none; }
  .contact__item span { margin-left: 13px; line-height: 1.3; }
  .contact__item--address { top: 4px; }
  .contact__item--address span { margin-left: 15px; margin-top: -2px; }
  .contact__item--phone { top: 42px; }
  .contact__item--web { top: 73px; }

  .hours-title {
    position: absolute; left: 215px; top: 214px; width: 168px; height: 24px;
    background: linear-gradient(90deg, var(--gold-dark), var(--gold-light) 50%, var(--gold-dark));
    font-family: "Cinzel", serif; font-weight: 700; font-size: 15px;
    color: var(--ink-dark); text-align: center; line-height: 25px;
  }
  .hours { position: absolute; left: 0; top: 242px; width: 100%;
    font-family: "Open Sans", sans-serif; font-size: 12.5px; color: var(--white); }
  .hours__row { position: absolute; left: 0; width: 100%; height: 16px; }
  .hours__row:nth-child(2) { top: 16px; }
  .hours__row span { position: absolute; top: 0; }
  .hours__day { font-weight: 600; }
  .c1 { left: 29px; } .c2 { left: 128px; } .c3 { left: 206px; } .c4 { left: 247px; }
  .c5 { left: 316px; } .c6 { left: 416px; } .c7 { left: 494px; } .c8 { left: 533px; }
</style>
</head>
<body>
<main class="board">

  <section class="card card--front" aria-label="Business card front">
    <div class="brand">
      <span class="brand__dot"></span>
      <div class="brand__name">Maple Ridge</div>
      <div class="brand__sub">Family Chiropractic</div>
    </div>
    <div class="gold-band"></div>
    <h1 class="doctor">Dr. Warren Balfour Chiropractor</h1>
    <ul class="contact">
      <li class="contact__item contact__item--address">
        <svg viewBox="0 0 24 24" aria-hidden="true"><path d="M12 2 1 11h3v11h6v-6h4v6h6V11h3z" fill="#fff"/></svg>
        <span>214 Pellham R. Road Alder Falls,<br>NY 13752</span>
      </li>
      <li class="contact__item contact__item--phone">
        <svg viewBox="0 0 24 24" aria-hidden="true"><circle cx="12" cy="12" r="10.5" fill="none" stroke="#fff" stroke-width="1.4"/><path d="M8.6 6.5c.4-.3.9-.2 1.1.2l1 1.8c.2.4.1.8-.2 1.1l-.7.6c.5 1.3 1.6 2.6 2.9 3.2l.6-.7c.3-.3.8-.4 1.1-.2l1.8 1c.4.2.5.8.2 1.1l-.8 1c-.6.6-1.5.8-2.3.4-2.7-1.2-4.7-3.4-5.8-6.1-.3-.8 0-1.6.5-2.1z" fill="#fff"/></svg>
        <span>607-555-0184</span>
      </li>
      <li class="contact__item contact__item--web">
        <svg viewBox="0 0 24 24" aria-hidden="true"><g fill="none" stroke="#fff" stroke-width="1.4"><circle cx="12" cy="12" r="10.5"/><ellipse cx="12" cy="12" rx="4.5" ry="10.5"/><path d="M1.5 12h21M12 1.5v21"/></g></svg>
        <span>www.vitalspringcare.com</span>
      </li>
    </ul>
  </section>

  <section class="card card--back" aria-label="Business card back">
    <div class="brand">
      <span class="brand__dot"></span>
      <div class="brand__name">Maple Ridge</div>
      <div class="brand__sub">Family Chiropractic</div>
    </div>
    <h2 class="hours-title">Office Hours:</h2>
    <div class="hours">
      <div class="hours__row">
        <span class="hours__day c1">Monday</span><span class="c2">Date 9-12,</span><span class="c3">Time</span><span class="c4">2:30-5</span>
        <span class="hours__day c5">Wednesday</span><span class="c6">Date 9-12,</span><span class="c7">Time</span><span class="c8">2:30-5</span>
      </div>
      <div class="hours__row">
        <span class="hours__day c1">Tuesday</span><span class="c3">Time</span><span class="c4">2:30-6</span>
        <span class="hours__day c5">Thursday</span><span class="c6">Date 9-12,</span><span class="c7">Time</span><span class="c8">2:30-6</span>
      </div>
    </div>
  </section>

</main>
</body>
</html>
```